Ablaufgrafik FlussWerkzeug
Zielgruppe
FlussWerkzeug: Content Marketing-Lösung für KMU
Ohne Aufwand verleiht FlussWerkzeug Inhalten (Produkt-Meldungen, Presse-Mitteilungen, Blog-Artikel, …) die notwendige Reichweite um Neukundenkontakte zu generieren.
Der Content geht über alle Kanäle: Web, Mail und Social.
Der FlussWerkzeug bietet flexible und maßgeschneiderte Online Marketing Lösungen, die sich am Bedarf hinsichtlich Quantität, Qualität, den Kunden-Bedürfnissen und dem Budget angleichen. Bis hin zu individuell selektierten Verteilern.
Aufgabenstellung
Es soll eine Ablaufgrafik erstellt werden, die visualisiert "Was passiert mit meinem Content über den FlussWerkzeug": Eine Prozess-Visualisierung.
Die Ablaufgrafik wird als JPG/PNG bei flusswerkzeug.de eingebunden: Mit klick öffnet sich eine bildschirmfüllende Grafik. Ebenso soll die Grafik im factsheet (pdf) eingebunden werden.
- CI gemäß www.flusswerkzeug.de
- Anschauung und Info: factsheet-PDF http://kurzlink-beispiel.de/a7Rt2K
- Logo: http://kurzlink-beispiel.de/m3Vw9P
Skizze zum Aufbau und den Inhalten für die Ablaufgrafik: s. Dateianlage (pdf)

```html
<!DOCTYPE html>
<html lang="de">
<head>
<meta charset="utf-8">
<title>FlussWerkzeug – Ablaufgrafik</title>
<link href="https://fonts.googleapis.com/css2?family=Open+Sans:wght@400;600;700&display=swap" rel="stylesheet">
<style>
  :root {
    --ink: #3d4450;
    --text: #545a61;
    --line: #d9dcdd;
    --sky: #56c2e1;
    --teal: #6cc5bf;
    --blue: #16a7da;
    --white: #ffffff;
  }
  html, body {
    margin: 0;
    padding: 0;
    width: 1200px;
    height: 2324px;
    overflow: hidden;
    background: var(--white);
    font-family: "Open Sans", sans-serif;
  }
  .sheet {
    position: relative;
    width: 1330px;
    height: 2576px;
    transform: scale(0.90226);
    transform-origin: 0 0;
  }
  .layer { position: absolute; left: 0; top: 0; }

  .brand {
    position: absolute; left: 113px; top: 78px;
    display: flex; align-items: center; gap: 14px;
  }
  .brand-mark { width: 54px; height: 54px; background: var(--sky); }
  .brand-name { font-size: 42px; font-weight: 600; color: var(--ink); letter-spacing: -0.5px; }

  .step {
    position: absolute; left: 0; width: 415px; height: 74px;
    display: flex;
  }
  .step-label {
    width: 327px; background: var(--ink); color: var(--white);
    font-size: 33px; display: flex; align-items: center; justify-content: center;
    letter-spacing: 0.5px;
  }
  .step-label b { font-weight: 700; margin-right: 10px; }
  .step-accent { flex: 1; background: var(--sky); }

  .hub {
    position: absolute; height: 63px;
    background: linear-gradient(90deg, var(--teal), var(--blue));
    color: var(--white); font-size: 30px; font-weight: 600;
    display: flex; align-items: center; justify-content: center;
  }

  .box {
    position: absolute; box-sizing: border-box;
    border: 2px solid var(--line); background: var(--white);
    color: var(--text); font-size: 23px; line-height: 1.35;
    display: flex; flex-direction: column; align-items: center; justify-content: center;
    text-align: center;
  }
  .box p { margin: 0; }
  .box p + p { margin-top: 22px; }

  .channel-label {
    position: absolute; width: 182px; text-align: center;
    color: var(--white); font-size: 30px; line-height: 40px;
  }

  .slogan {
    position: absolute; left: 412px; top: 2454px; width: 503px; height: 69px;
    font-size: 23px; font-weight: 600; color: var(--ink);
  }
</style>
</head>
<body>
<div class="sheet">

  <svg class="layer decor" width="1330" height="2576" viewBox="0 0 1330 2576" aria-hidden="true">
    <defs>
      <radialGradient id="corner-glow" cx="1" cy="0" r="1">
        <stop offset="0" stop-color="#3fb0d0"/>
        <stop offset="0.5" stop-color="#7cc8cf" stop-opacity="0.7"/>
        <stop offset="1" stop-color="#ffffff" stop-opacity="0"/>
      </radialGradient>
      <linearGradient id="people" x1="249" y1="0" x2="1079" y2="0" gradientUnits="userSpaceOnUse">
        <stop offset="0" stop-color="#6cc5bf"/>
        <stop offset="1" stop-color="#16a7da"/>
      </linearGradient>
    </defs>

    <rect x="640" y="0" width="690" height="700" fill="url(#corner-glow)"/>

    <g class="connectors" fill="none" stroke="#d9dcdd" stroke-width="2">
      <path d="M665 393 V460 M486 460 H840 M486 460 V518 M840 460 V518"/>
      <path d="M466 498 L486 518 L506 498 M820 498 L840 518 L860 498"/>
      <path d="M486 591 V658 H840 V591 M665 658 V716"/>
      <path d="M645 696 L665 716 L685 696"/>
      <path d="M665 789 V852 M315 852 H1017 M315 852 V902 M665 852 V902 M1017 852 V902"/>
      <path d="M295 882 L315 902 L335 882 M645 882 L665 902 L685 882 M997 882 L1017 902 L1037 882"/>
      <path d="M315 1094 V1157 M665 1094 V1157 M1017 1094 V1157"/>
      <path d="M295 1137 L315 1157 L335 1137 M645 1137 L665 1157 L685 1137 M997 1137 L1017 1157 L1037 1137"/>
      <path d="M315 1271 V1291 M665 1361 V1381 M665 1451 V1471 M1017 1237 V1257 M1017 1327 V1347"/>
      <path d="M315 1361 V1590 H1017 V1417 M665 1541 V1703"/>
      <path d="M645 1683 L665 1703 L685 1683"/>
      <path d="M665 1890 V1965 M665 2038 V2112 M665 2365 V2440"/>
      <path d="M645 1945 L665 1965 L685 1945 M645 2092 L665 2112 L685 2092 M645 2420 L665 2440 L685 2420"/>
    </g>

    <g class="channels">
      <circle cx="315" cy="1003" r="91" fill="#56c2e1"/>
      <circle cx="665" cy="1003" r="91" fill="#56c2e1"/>
      <circle cx="1017" cy="1003" r="91" fill="#56c2e1"/>
    </g>
    <g class="channel-icons" fill="none" stroke="#ffffff" stroke-width="3" stroke-linejoin="round">
      <path d="M302 962 L328 980 L316 983 L322 996 L316 999 L310 986 L302 994 Z"/>
      <rect x="643" y="962" width="44" height="32" rx="2"/>
      <path d="M643 964 L665 982 L687 964"/>
      <path d="M995 962 H1039 V988 H1010 L1000 997 V988 H995 Z"/>
    </g>

    <g class="audience" fill="url(#people)">
      <circle cx="290" cy="1756" r="41"/><circle cx="383" cy="1756" r="41"/><circle cx="477" cy="1756" r="41"/>
      <circle cx="570" cy="1756" r="41"/><circle cx="664" cy="1756" r="41"/><circle cx="758" cy="1756" r="41"/>
      <circle cx="851" cy="1756" r="41"/><circle cx="944" cy="1756" r="41"/><circle cx="1038" cy="1756" r="41"/>
      <circle cx="290" cy="1848" r="41"/><circle cx="383" cy="1848" r="41"/><circle cx="477" cy="1848" r="41"/>
      <circle cx="570" cy="1848" r="41"/><circle cx="664" cy="1848" r="41"/><circle cx="758" cy="1848" r="41"/>
      <circle cx="851" cy="1848" r="41"/><circle cx="944" cy="1848" r="41"/><circle cx="1038" cy="1848" r="41"/>
    </g>
    <g class="audience-icons" fill="none" stroke="#ffffff" stroke-width="1.6">
      <g id="person">
        <circle cx="290" cy="1748" r="10"/>
        <path d="M272 1774 C274 1762 282 1758 290 1758 C298 1758 306 1762 308 1774 Z"/>
      </g>
      <use href="#person" x="93"/><use href="#person" x="187"/><use href="#person" x="280"/>
      <use href="#person" x="374"/><use href="#person" x="468"/><use href="#person" x="561"/>
      <use href="#person" x="654"/><use href="#person" x="748"/>
      <use href="#person" y="92"/><use href="#person" x="93" y="92"/><use href="#person" x="187" y="92"/>
      <use href="#person" x="280" y="92"/><use href="#person" x="374" y="92"/><use href="#person" x="468" y="92"/>
      <use href="#person" x="561" y="92"/><use href="#person" x="654" y="92"/><use href="#person" x="748" y="92"/>
    </g>

    <circle cx="665" cy="2245" r="120" fill="#56c2e1"/>
    <rect x="588" y="2188" width="164" height="120" rx="10" fill="#e8eef1" opacity="0.85"
          role="img" aria-label="Illustration: Laptop mit Auswertungsdiagrammen und Lupe"/>
  </svg>

  <div class="brand">
    <span class="brand-mark"></span>
    <span class="brand-name">FlussWerkzeug</span>
  </div>

  <div class="step" style="top:324px"><div class="step-label"><b>1.</b>ERSTELLEN</div><div class="step-accent"></div></div>
  <div class="step" style="top:722px"><div class="step-label"><b>2.</b>VERBREITEN</div><div class="step-accent"></div></div>
  <div class="step" style="top:1968px"><div class="step-label"><b>3.</b>AUSWERTEN</div><div class="step-accent"></div></div>

  <div class="hub" style="left:541px; top:330px; width:243px;">Ihre News</div>
  <div class="hub" style="left:534px; top:726px; width:258px;">Ihr Newsroom</div>
  <div class="hub" style="left:534px; top:1975px; width:258px;">Ihre Kunden</div>

  <div class="box" style="left:358px; top:529px; width:197px; height:63px;">Mail</div>
  <div class="box" style="left:771px; top:529px; width:197px; height:63px;">Login</div>

  <div class="channel-label" style="left:224px; top:1018px;">Web</div>
  <div class="channel-label" style="left:574px; top:1018px;">Mail</div>
  <div class="channel-label" style="left:926px; top:1018px;">Social</div>

  <div class="box" style="left:160px; top:1167px; width:299px; height:105px;">Portale<br>im Medien-Netzwerk</div>
  <div class="box" style="left:160px; top:1291px; width:299px; height:71px;">Suchfix &amp; Co.</div>

  <div class="box" style="left:515px; top:1167px; width:299px; height:195px;">
    <p>Marketing-Verteiler</p>
    <p>Fach-/führungskräfte,<br>Entscheider,<br>Meinungsmacher, …</p>
  </div>
  <div class="box" style="left:515px; top:1381px; width:299px; height:71px;">Journalisten-Verteiler</div>
  <div class="box" style="left:515px; top:1471px; width:299px; height:71px;">Individuelle-Verteiler</div>

  <div class="box" style="left:871px; top:1167px; width:299px; height:71px;">Freundesnetz</div>
  <div class="box" style="left:871px; top:1257px; width:299px; height:71px;">Kurzfunk</div>
  <div class="box" style="left:871px; top:1347px; width:299px; height:71px;">Berufsnetz</div>

  <div class="box slogan">Einfach. Erfolgreich. Kunden gewinnen.</div>
</div>
</body>
</html>
```